Banner photo design to use for our marketing products

We need a banner photo for landing page of our website and to use in our other marketing products. We need it to reflect the idea of that "we are drowning in data but starving for information". Our company is a software- internet of things company that creates products to help companies have meaningful insights from their big and complicated data. We like simple designs, which reflects just our concerns and no more than that. Here is our website www.corvanteq.com. When you click on the link, you will see blue pictures in the landing page. Basically, we want to replace it/them with the new design. The text you will see on the banner is added by us later on, so you do not need to add the text to your designs as it is better for us if the text is changeable.
Target Market(s)
Software company customers, decision makers of all industries that is actively working with data.
Industry/Entity Type
Software
Requirements
Must have
- Our project should reflect the idea of creating meanings from huge and complicated data. It must arouse curiosity for customers feeling stuck in huge data to dig deeper in our website.
Nice to have
- It may have an idea to say how can our company can change the way things go traditionally. In our current landing page, you will see a mountain and then a diamond. Idea was, there are mountains of data but we know how to dig into your information diamonds. New design can also stay on this track or could be more creative.. We not only help collecting meaningful data but also visualize them. So it may nice to have it.
Should not have
- We do not like indirect messages and full-colored designs. We want to reflect the way of Nordic companies marketing, which is simple and direct.

```html
<!DOCTYPE html>
<html lang="en">
<head>
<meta charset="utf-8">
<title>Drowning in Data – Hero Banner</title>
<link href="https://fonts.googleapis.com/css2?family=Josefin+Sans:wght@600;700&display=swap" rel="stylesheet">
<style>
  :root {
    --sky-light: #a6d6ff;
    --sky-mid: #7dbcff;
    --sky-deep: #4f95ff;
    --wave-soft: rgba(255, 255, 255, 0.12);
    --wave-deep: #5a9fff;
    --wave-deeper: #4a8cfb;
    --gem-light: #8fe6f0;
    --gem-mid: #2fb7cf;
    --gem-deep: #147fa8;
    --headline: #f4f4f2;
    --button-bg: #ffffff;
    --button-text: #1f6c86;
  }
  * { margin: 0; padding: 0; box-sizing: border-box; }
  html, body {
    width: 1200px;
    height: 960px;
    overflow: hidden;
  }
  body {
    font-family: "Josefin Sans", "Century Gothic", sans-serif;
  }
  .hero {
    position: relative;
    width: 1200px;
    height: 960px;
    overflow: hidden;
    background: linear-gradient(200deg, var(--sky-light) 0%, var(--sky-mid) 45%, var(--sky-deep) 100%);
  }
  .hero__waves {
    position: absolute;
    inset: 0;
    width: 1200px;
    height: 960px;
  }
  .hero__gem {
    position: absolute;
    left: 40px;
    top: 110px;
    width: 440px;
    height: 420px;
    border-radius: 50%;
    background:
      radial-gradient(ellipse 60% 45% at 50% 48%, var(--gem-light) 0%, var(--gem-mid) 45%, var(--gem-deep) 70%, rgba(20, 127, 168, 0) 72%),
      radial-gradient(ellipse 50% 50% at 50% 40%, rgba(255, 255, 255, 0.55) 0%, rgba(255, 255, 255, 0) 70%);
  }
  .hero__headline {
    position: absolute;
    left: 640px;
    top: 150px;
    color: var(--headline);
    font-weight: 700;
    font-size: 60px;
    line-height: 72px;
    letter-spacing: 3px;
    text-transform: uppercase;
    transform: rotate(1.5deg);
    transform-origin: left top;
  }
  .hero__headline .outline {
    color: transparent;
    -webkit-text-stroke: 2px var(--headline);
    font-weight: 600;
    letter-spacing: 5px;
  }
  .hero__headline .outline--wide {
    font-size: 58px;
    letter-spacing: 6px;
  }
  .hero__tagline {
    position: absolute;
    left: 0;
    right: 0;
    top: 690px;
    text-align: center;
    color: var(--headline);
    font-weight: 700;
    font-size: 34px;
    letter-spacing: 2px;
    text-transform: uppercase;
    transform: rotate(1.5deg);
  }
  .hero__cta {
    position: absolute;
    left: 480px;
    top: 770px;
    width: 250px;
    height: 80px;
    border-radius: 40px;
    background: var(--button-bg);
    color: var(--button-text);
    font-weight: 700;
    font-size: 28px;
    letter-spacing: 1.5px;
    text-transform: uppercase;
    display: flex;
    align-items: center;
    justify-content: center;
    padding-top: 6px;
    transform: rotate(1.5deg);
    box-shadow: 0 6px 18px rgba(30, 80, 160, 0.18);
  }
</style>
</head>
<body>
  <main class="hero">
    <svg class="hero__waves" viewBox="0 0 1200 960" aria-hidden="true">
      <circle cx="470" cy="330" r="390" fill="var(--wave-soft)"/>
      <path d="M0 560 C 180 450, 360 470, 560 600 S 900 540, 1200 620 L1200 960 L0 960 Z" fill="var(--wave-deep)" opacity="0.55"/>
      <path d="M0 600 C 200 700, 420 720, 620 620 S 950 520, 1200 640 L1200 960 L0 960 Z" fill="var(--wave-deep)" opacity="0.7"/>
      <path d="M0 820 C 220 760, 420 800, 620 880 S 950 860, 1200 900 L1200 960 L0 960 Z" fill="var(--wave-deeper)" opacity="0.6"/>
      <circle cx="130" cy="40" r="3" fill="#ffffff"/>
      <circle cx="70" cy="175" r="4" fill="#ffffff"/>
      <circle cx="115" cy="465" r="3" fill="#ffffff"/>
      <circle cx="330" cy="540" r="3" fill="#ffffff"/>
      <circle cx="1100" cy="55" r="3" fill="#ffffff"/>
      <circle cx="1150" cy="440" r="3" fill="#ffffff"/>
    </svg>

    <div class="hero__gem" role="img" aria-label="Illustration of a glowing faceted teal diamond with light rays behind it"></div>

    <h1 class="hero__headline">
      The world<br>
      is drowning<br>
      in <span class="outline">data</span> but<br>
      starving for<br>
      <span class="outline outline--wide">information</span>
    </h1>

    <p class="hero__tagline">Our customers are not</p>

    <a class="hero__cta">Here is why</a>
  </main>
</body>
</html>
```